Yoga site design

we need to design a homepage and content sections for our yoga portal

Palvenora

Palvenora is a yoga community ecosystem dedicated to the yoga enthusiasts and adopters of an active lifestyle based upon yoga and ayurvedic living. The objective of Palvenora is to expand the involvment and adoption of yoga across the communities and facilitate the profitable growth of the various stakeholders and service providers involved with the ecosystem

Site descriptor

The site will have 4 building blocks/functionalities as specified below;

1.Directory functionality wherein it would list yoga classes/events/ workshop/ retreats and show calendar by dates and place
1. when
2. where
3. what
4. who
5. cost
6. durations

2.Search functionality

a.Find a yoga class/studio close to you (location tagging/google maps)
search/show by studioname/ teacher/ Private sessions/ yoga family
1. when
2. where
3. what
4. who
5. cost

3.Content publishing capabilty

a.Micro sites studio directory/ teachers/ frequent event holders/ therapists - contributors and serviceproviders
1. words of descriprion about yourself and your business
2. an email address
3. a live web link
4. google maps
5. contact phone number
6. a logo upload
7. a picture of themselves, (we need to specify size)
8 Weekly/monthly calendar - where thay are and when

b.Topical content
• columns written by a refference or celebrity
• parts in Montly newsletter and/or downloadable

c.Monthly Newsletter

d.What is New/News/Flash Happenings on the Site

e.Community Board
a virtual meeting place on a login and username basis
• Twitter
• chat
• yoganetwork - offline community build
• find a group close to you!

4.E-commerce capability (Yoga store)
by category;
• yoga props
• yoga clothes
• Ayurvedic related products
• Books/Music/dvd
• skin/body
tickets to events -

yoga enthusiasts across multiple cities in europe and americas

• the design should not be intrusive and allow for multiple city instances to be created using the same deisgn sensibilities
• i do not need any tech coding.

```html
<!DOCTYPE html>
<html lang="en">
<head>
<meta charset="utf-8">
<title>Palvenora – Yoga Community</title>
<link href="https://fonts.googleapis.com/css2?family=Arimo:ital,wght@0,400;0,700;1,700&family=Oswald:wght@600&display=swap" rel="stylesheet">
<style>
:root{
  --teal:#0e8699;
  --teal-dark:#0b6f80;
  --cyan:#17c3e0;
  --heading:#13879a;
  --text-green:#1f5a40;
  --text:#333;
  --grey:#8a8a8a;
  --row:#ededed;
  --page:#f4f6f6;
  --white:#fff;
}
*{box-sizing:border-box;margin:0;padding:0}
html,body{width:1101px;height:1200px;overflow:hidden;background:var(--page)}
body{font-family:"Arimo",Arial,sans-serif;color:var(--text)}
.stage{position:absolute;left:0;top:0;width:1003px;height:1093px;transform:scale(1.0977);transform-origin:0 0;background:var(--page)}
.abs{position:absolute}

.top-stripe{left:0;top:0;width:1003px;height:4px;background:var(--teal)}
.header{left:0;top:4px;width:1003px;height:94px;background:linear-gradient(180deg,#e4f4f4,#f7fbfb 60%,#e9f4f4)}
.brand{left:44px;top:28px;font-size:32px;font-weight:700;color:var(--teal);letter-spacing:.5px}
.call{left:765px;top:33px;font-size:24px;color:#555}
.call b{color:#444}

.nav{left:0;top:98px;width:1003px;height:34px;background:var(--teal)}
.nav ul{list-style:none;display:flex;height:34px;padding-left:33px}
.nav li{font-size:12px;color:var(--white);line-height:34px;padding:0 16px;border-right:1px solid #2a9aab}
.nav li.active{background:var(--cyan)}
.search{left:773px;top:103px;width:216px;height:24px;background:var(--white);border:1px solid #cfd8da;font-size:11px;color:#aaa;padding:5px 7px}

.content{left:30px;top:132px;width:960px;height:830px;background:var(--white)}
.divider{left:318px;top:140px;width:1px;height:815px;background:#eceeee}

.chat{left:52px;top:158px;width:249px;height:32px;background:linear-gradient(180deg,#2ab8cf,#0f93a8);border-radius:3px}
.chat-icon{left:54px;top:146px;width:30px;height:30px;border-radius:50%;background:#6cbf4a;border:2px solid var(--white)}
.chat span{position:absolute;left:66px;top:5px;font-size:21px;font-weight:700;font-style:italic;color:var(--white)}

.side-h{font-size:17px;font-weight:400;color:var(--heading);left:53px;width:245px;padding-bottom:5px;border-bottom:1px dotted #9fcbd2}
.news{left:58px;width:238px;font-size:12.5px;line-height:19px;color:var(--text-green);text-align:justify;padding-left:10px}
.news::before{content:"";position:absolute;left:0;top:7px;width:4px;height:4px;background:var(--teal)}

.promo{left:44px;top:372px;width:258px;height:227px;border:1px solid #cdd;background:linear-gradient(180deg,#e4f2ea 0%,#8cc04a 100%)}
.promo p{position:absolute;left:20px;top:9px;font-size:21px;color:#14502c}

.event{left:49px;width:249px;border-bottom:1px solid #e3e3e3}
.event svg{position:absolute;left:0;top:0}
.event p{margin-left:39px;font-size:12.5px;line-height:19px;color:var(--text-green);text-align:justify}

.arrow-btn{top:876px;width:44px;height:28px;border:1px solid #cfcfcf;border-radius:5px;background:linear-gradient(180deg,#fdfdfd,#e2e2e2)}
.arrow-btn svg{position:absolute;left:14px;top:8px}

.hero{left:341px;top:151px;width:629px;height:251px;border:1px solid #e2e2e2;background:linear-gradient(180deg,#e3edf4 0%,#c9dfea 100%)}
.hero-title{left:368px;top:226px;font-family:"Oswald",Arial,sans-serif;font-size:29px;font-weight:600;color:#2f5470;letter-spacing:1px}

.welcome{left:342px;top:426px;font-size:21px;font-weight:700;color:var(--heading)}
.intro{left:345px;top:466px;width:614px;font-size:12.5px;line-height:19px;text-align:justify;color:#333}
.intro b{color:var(--teal)}

.schedule{left:344px;top:558px;width:627px;height:251px;border:1px solid #c9c9c9;border-radius:5px;background:var(--white)}
.sched-tab{left:346px;top:561px}
.sched-title{left:363px;top:567px;font-size:17px;font-weight:700;color:var(--white)}
.centers{left:822px;top:571px;width:136px;height:31px;border-radius:3px;background:linear-gradient(180deg,#f4f4f4,#cfcfcf);border:2px solid #555;border-right-color:#999;border-bottom-color:#999}
.centers span{position:absolute;left:12px;top:5px;font-size:16px;font-weight:700;color:#444}
.centers svg{position:absolute;right:8px;top:8px}
.days{left:362px;top:606px;font-size:14px;font-weight:700;color:#888}
.days .on{color:var(--teal)}
.days i{font-style:normal;margin:0 6px;color:#999;font-weight:400}
.today{left:363px;top:641px;font-size:13px;font-weight:700;color:#666}
.row{left:365px;width:558px;height:25px;background:var(--row);font-size:12.5px}
.row .code{position:absolute;left:0;top:0;width:57px;height:25px;color:var(--white);font-weight:700;text-align:center;line-height:25px;font-size:13px}
.row.a .code{background:var(--teal)}
.row.b .code{background:#a9a9a9}
.row span{position:absolute;top:6px}
.row .time{left:73px;color:#777;font-size:12px}
.row .name{left:183px;font-weight:700;font-size:13px}
.row.a .name{color:var(--teal)}
.row.b .name{color:#b0b0b0}
.row .desc,.row .reserve{color:var(--teal)}
.row .desc{left:273px}
.row .reserve{left:433px}
.scroll{left:931px;top:676px;width:13px;height:119px;background:#eee}
.thumb{left:931px;top:699px;width:13px;height:16px;background:var(--teal)}

.find{top:822px;width:145px;height:124px;border:1px solid #ddd;border-radius:4px;background:linear-gradient(180deg,#fff,#e4e4e4)}
.find p{position:absolute;left:11px;top:32px;font-size:18px;color:var(--heading)}
.find strong{display:block;font-size:16px;color:var(--teal-dark);margin-top:8px;line-height:22px}

.footer{left:0;top:962px;width:1003px;height:131px;background:var(--teal);border-top:2px solid #0a6d7c}
.foot-links{left:54px;top:981px;font-size:12px;color:var(--white)}
.foot-links i{font-style:normal;margin:0 5px}
.connect{left:53px;top:1012px;font-size:12px;color:var(--white)}
.social{top:1035px;width:18px;height:18px;border-radius:3px;background:#e7f3f6}
.copyright{left:911px;top:981px;font-size:12px;color:var(--white)}
</style>
</head>
<body>
<div class="stage">
  <div class="abs top-stripe"></div>
  <header class="abs header"></header>
  <div class="abs brand">PALVENORA</div>
  <div class="abs call">Call us : <b>+1 555 0192</b></div>

  <nav class="abs nav">
    <ul>
      <li>HOME</li><li class="active">YOGA</li><li>CLASSES</li><li>LOCATIONS</li><li>COMMUNITY</li><li>ABOUT</li><li>CONTACT US</li>
    </ul>
  </nav>
  <div class="abs search">Search</div>

  <div class="abs content"></div>
  <div class="abs divider"></div>

  <div class="abs chat"><span>24 x 7 Live Chat</span></div>
  <div class="abs chat-icon"></div>

  <h3 class="abs side-h" style="top:206px">What’s New</h3>
  <p class="abs news" style="top:239px">Lorem ispum dolor sit ipsum Lorem ispum dolor sit ipsum Lorem ispum dolor sit ipsum</p>
  <p class="abs news" style="top:315px">Lorem ispum dolor sit i psum Lorem ispum dolor sit ipsu</p>

  <div class="abs promo" role="img" aria-label="Photo of hands resting in a meditation pose on green grass"><p>Lorem Ipsum dolor sit</p></div>

  <h3 class="abs side-h" style="top:628px">Upcomming Events</h3>
  <div class="abs event" style="top:668px;height:64px">
    <svg width="26" height="24" viewBox="0 0 26 24"><rect x="1" y="3" width="24" height="20" rx="2" fill="#fff" stroke="#c33" stroke-width="1.5"/><rect x="1" y="3" width="24" height="6" fill="#d23b2a"/><text x="13" y="20" font-size="10" font-weight="700" text-anchor="middle" fill="#c33" font-family="Arimo,Arial,sans-serif">15</text></svg>
    <p>Lorem ispum dolor sit ipsum Lorem ispum dolor sit ipsum Lorem ispum dolor sit ipsum</p>
  </div>
  <div class="abs event" style="top:744px;height:51px">
    <svg width="26" height="24" viewBox="0 0 26 24"><rect x="1" y="3" width="24" height="20" rx="2" fill="#fff" stroke="#c33" stroke-width="1.5"/><rect x="1" y="3" width="24" height="6" fill="#d23b2a"/><text x="13" y="20" font-size="10" font-weight="700" text-anchor="middle" fill="#c33" font-family="Arimo,Arial,sans-serif">15</text></svg>
    <p>Lorem ispum dolor sit i psum Lorem ispum dolor sit ipsu</p>
  </div>
  <div class="abs event" style="top:801px;height:55px">
    <svg width="26" height="24" viewBox="0 0 26 24"><rect x="1" y="3" width="24" height="20" rx="2" fill="#fff" stroke="#c33" stroke-width="1.5"/><rect x="1" y="3" width="24" height="6" fill="#d23b2a"/><text x="13" y="20" font-size="10" font-weight="700" text-anchor="middle" fill="#c33" font-family="Arimo,Arial,sans-serif">15</text></svg>
    <p>Lorem ispum dolor sit i psum Lorem ispum dolor sit ipsu</p>
  </div>

  <div class="abs arrow-btn" style="left:49px"><svg width="16" height="12" viewBox="0 0 16 12"><path d="M0 6 L7 0 V4 H15 V8 H7 V12 Z" fill="#222"/></svg></div>
  <div class="abs arrow-btn" style="left:103px"><svg width="16" height="12" viewBox="0 0 16 12"><path d="M16 6 L9 0 V4 H1 V8 H9 V12 Z" fill="#222"/></svg></div>

  <div class="abs hero" role="img" aria-label="Photo of a woman holding a warrior yoga pose on a sunny beach"></div>
  <div class="abs hero-title">PERFECT FIT YOUR LIFE</div>

  <h1 class="abs welcome">Welcome &nbsp;to Palvenora</h1>
  <p class="abs intro">Palvenora is a yoga community ecosystem dedicated to the yoga enthusiasts and adopters of an active lifestyle based upon yoga and ayurvedic living. The objective of Palvenora is to expand the involvment and adoption of yoga across the communities and facilitate the profitable growth of the various stakeholders and service providers involved with the ecosystem &nbsp;<b>More..</b></p>

  <section class="abs schedule"></section>
  <svg class="abs sched-tab" width="412" height="34" viewBox="0 0 412 34"><defs><linearGradient id="tabfill" x1="0" y1="0" x2="0" y2="1"><stop offset="0" stop-color="#2cc0d8"/><stop offset="1" stop-color="#0d8fa4"/></linearGradient></defs><path d="M0 4 Q0 0 4 0 H412 Q392 6 380 34 H0 Z" fill="url(#tabfill)"/></svg>
  <h2 class="abs sched-title">Upcoming Class Schedule</h2>
  <div class="abs centers"><span>All Centers</span><svg width="20" height="14" viewBox="0 0 20 14"><path d="M2 2 L10 11 L18 2" fill="none" stroke="#0e8699" stroke-width="4"/></svg></div>
  <div class="abs days"><span class="on">Sat</span><i>I</i>Sun<i>I</i>Mon<i>I</i>Tue<i>I</i>Wed<i>I</i>Thu<i>I</i>Fri</div>
  <div class="abs today">Today Aug 30, 2011</div>

  <div class="abs row a" style="top:676px"><div class="code">XYZ</div><span class="time">12:00 - 1.00 pm</span><span class="name">XYZ</span><span class="desc">Lorem ipsum</span><span class="reserve">Reserve</span></div>
  <div class="abs row b" style="top:707px"><div class="code">XYZ</div><span class="time">12:00 - 1.00 pm</span><span class="name">XYZ</span><span class="desc">Lorem ipsum</span><span class="reserve">Reserve</span></div>
  <div class="abs row a" style="top:738px"><div class="code">XYZ</div><span class="time">12:00 - 1.00 pm</span><span class="name">XYZ</span><span class="desc">Lorem ipsum</span><span class="reserve">Reserve</span></div>
  <div class="abs row b" style="top:769px"><div class="code">XYZ</div><span class="time">12:00 - 1.00 pm</span><span class="name">XYZ</span><span class="desc">Lorem ipsum</span><span class="reserve">Reserve</span></div>
  <div class="abs scroll"></div>
  <div class="abs thumb"></div>

  <div class="abs find" style="left:344px"><p>Find a<strong>STUDIO/CLASS</strong></p></div>
  <div class="abs find" style="left:504px"><p>Find an<strong>EVENT /<br>WORKSHOP</strong></p></div>
  <div class="abs find" style="left:665px"><p>Find a<strong>TEACHER</strong></p></div>
  <div class="abs find" style="left:825px"><p>Find a<strong>ADVERTISE US</strong></p></div>

  <footer class="abs footer"></footer>
  <div class="abs foot-links">HOME<i>I</i>YOGA<i>I</i>CLASSES<i>I</i>LOCATIONS<i>I</i>COMMUNITY<i>I</i>ABOUT<i>I</i>CONTACT US</div>
  <div class="abs connect">Connect to us :</div>
  <div class="abs social" style="left:53px"></div>
  <div class="abs social" style="left:83px"></div>
  <div class="abs copyright">Copyright Text</div>
</div>
</body>
</html>
```